Woman owned consulting company needs an elegant and modern business card design

I need a business card design for my new consulting company, Mara Quill Consulting. I am looking for something that is simple and elegant, but also creative and original. You can use either version of the logo that are attached. I have also included the information that needs to be featured on the business card.

Requirements
Must have
• The logo and the font type and a standard business card size. Use shades of gray/silver and or rose gold that are in the logo.
• I didn't realize that my actual logo wasn't attached. Please incorporate in the designs.
Should not have
• Colors that are different from my logo

```html
<!DOCTYPE html>
<html lang="en">
<head>
<meta charset="utf-8">
<title>Mara Quill Consulting — Business Card</title>
<link rel="stylesheet" href="https://fonts.googleapis.com/css2?family=Cormorant+Garamond:wght@600&family=Roboto:wght@400&display=swap">
<style>
  :root {
    --backdrop: #2b2b2d;
    --card: #6f6f70;
    --card-edge: #7a7a7b;
    --blush: #f6e8dd;
    --ink: #3b3b3c;
    --white: #ffffff;
  }
  * { margin: 0; padding: 0; box-sizing: border-box; }
  html, body { width: 1200px; height: 1200px; overflow: hidden; }
  body {
    background: var(--backdrop);
    display: flex;
    flex-direction: column;
    align-items: center;
    justify-content: center;
    gap: 60px;
  }
  .card {
    position: relative;
    width: 770px;
    height: 440px;
    background: var(--card);
    border-radius: 28px;
    box-shadow: 0 18px 40px rgba(0,0,0,.45);
  }
  .card-front {
    display: flex;
    align-items: center;
    justify-content: center;
  }
  .brand-name {
    font-family: "Cormorant Garamond", serif;
    font-weight: 600;
    line-height: 1;
    letter-spacing: .02em;
  }
  .card-front .brand-name {
    color: var(--blush);
    font-size: 64px;
  }
  .card-back .brand-name {
    position: absolute;
    top: 118px;
    left: 240px;
    color: var(--ink);
    font-size: 52px;
  }
  .contact-block {
    position: absolute;
    right: 70px;
    bottom: 52px;
    text-align: right;
  }
  .person-name {
    font-family: "Cormorant Garamond", serif;
    font-weight: 600;
    font-size: 30px;
    color: var(--blush);
    letter-spacing: .02em;
  }
  .person-role {
    font-family: "Roboto", sans-serif;
    font-size: 17px;
    color: var(--white);
    margin-top: 2px;
  }
  .divider {
    width: 34px;
    height: 2px;
    background: var(--blush);
    margin: 14px 0 14px auto;
  }
  .contact-list { list-style: none; }
  .contact-list li {
    display: flex;
    align-items: center;
    justify-content: flex-end;
    gap: 12px;
    font-family: "Roboto", sans-serif;
    font-size: 19px;
    color: var(--white);
    line-height: 30px;
  }
  .contact-list svg { width: 20px; height: 20px; flex: none; }
</style>
</head>
<body>

  <section class="card card-front" aria-label="Card front">
    <h1 class="brand-name">Mara Quill Consulting</h1>
  </section>

  <section class="card card-back" aria-label="Card back">
    <p class="brand-name">Mara Quill Consulting</p>

    <div class="contact-block">
      <p class="person-name">MARA QUILL</p>
      <p class="person-role">Owner</p>
      <div class="divider"></div>
      <ul class="contact-list">
        <li>610-555-0147
          <svg viewBox="0 0 24 24" fill="none" stroke="#f6e8dd" stroke-width="1.8" stroke-linecap="round" stroke-linejoin="round" aria-hidden="true">
            <path d="M5 3h4l2 5-2.5 1.5a11 11 0 0 0 6 6L16 13l5 2v4a2 2 0 0 1-2 2A16 16 0 0 1 3 5a2 2 0 0 1 2-2z"/>
          </svg>
        </li>
        <li>mara@maraquillconsulting.com
          <svg viewBox="0 0 24 24" fill="none" stroke="#f6e8dd" stroke-width="1.8" stroke-linejoin="round" aria-hidden="true">
            <rect x="3" y="6" width="18" height="13" rx="1.5"/>
            <path d="M3 7l9 7 9-7"/>
          </svg>
        </li>
        <li>www.maraquillconsulting.com
          <svg viewBox="0 0 24 24" fill="none" stroke="#f6e8dd" stroke-width="1.6" aria-hidden="true">
            <circle cx="12" cy="12" r="9"/>
            <ellipse cx="12" cy="12" rx="4" ry="9"/>
            <path d="M3 12h18M5 7h14M5 17h14"/>
          </svg>
        </li>
      </ul>
    </div>
  </section>

</body>
</html>
```